Toravelle Works Luxury Candles

Luxury box design,, simple and sophisticated look,,

My collection of candles come in 5 different fragrances, i would like to be able to change the fragrance name on the boxes,,,,

I would like the outline of australia on the front down the bottom , (only small) to represent this is an australian product.

My boxes are white gloss,,,

Happy for you to use my current logo ,,, however you'll have to change Toravelle Nails to Toravelle Works.

```html
<!DOCTYPE html>
<html lang="en">
<head>
<meta charset="utf-8">
<title>Toravelle Works – Candle Box Front Panel</title>
<link rel="stylesheet" href="https://fonts.googleapis.com/css2?family=Open+Sans:wght@800&family=Oswald:wght@400;500;600&family=Pinyon+Script&display=swap">
<style>
  :root {
    --backdrop: #cdcdcd;
    --panel-light: #fbfbfb;
    --panel-mid: #e9e9ea;
    --panel-edge: #bdbdbd;
    --gold-deep: #8a6410;
    --gold-mid: #c79a22;
    --gold-bright: #f0d36a;
    --gold-text: #b8860b;
    --brown-text: #6b4a12;
    --ink: #1e1a14;
    --line-grey: #b9b9bb;
  }
  * { margin: 0; padding: 0; box-sizing: border-box; }
  html, body { width: 1200px; height: 782px; overflow: hidden; background: var(--backdrop); }
  .canvas { position: relative; width: 1200px; height: 782px; }

  .box-front {
    position: absolute; left: 297px; top: 21px; width: 605px; height: 740px;
    border: 1px solid var(--panel-edge);
    background:
      repeating-linear-gradient(0deg, rgba(255,255,255,0.35) 0 1px, rgba(0,0,0,0.025) 1px 3px),
      linear-gradient(90deg, var(--panel-mid), var(--panel-light) 30%, var(--panel-mid) 55%, var(--panel-light) 80%, var(--panel-mid));
    overflow: hidden;
  }

  .ornament-band {
    position: absolute; left: 0; top: 57px; width: 100%; height: 219px;
    background: linear-gradient(180deg, #efe3bf, #e6d08f 50%, #efe3bf);
    opacity: 0.85;
  }

  .brand-plate {
    position: absolute; left: 67px; top: 96px; width: 470px; height: 139px;
    background: linear-gradient(90deg, var(--gold-mid), var(--gold-bright) 45%, var(--gold-mid) 75%, var(--gold-deep));
    border: 2px solid var(--gold-bright);
    display: flex; align-items: center; justify-content: center;
  }
  .brand-name {
    font-family: "Pinyon Script", cursive;
    font-size: 58px; color: var(--ink); font-weight: 400;
  }

  .fragrance-title {
    position: absolute; left: 87px; top: 342px;
    font-family: "Open Sans", sans-serif; font-weight: 800;
    font-size: 60px; line-height: 52px; letter-spacing: -2.5px;
    color: var(--gold-text);
    background: linear-gradient(180deg, #d9a92a, #a87812 60%, #c9961f);
    -webkit-background-clip: text; background-clip: text; -webkit-text-fill-color: transparent;
  }

  .product-details { position: absolute; left: 87px; top: 460px; display: flex; }
  .craft-note { padding-right: 7px; border-right: 1.5px solid var(--brown-text); }
  .craft-heading {
    font-family: "Oswald", sans-serif; font-weight: 600; font-size: 29px; line-height: 30px;
    color: var(--brown-text); letter-spacing: -0.5px;
  }
  .craft-line {
    font-family: "Oswald", sans-serif; font-weight: 400; font-size: 11px; line-height: 13px;
    color: var(--brown-text);
  }
  .spec-list { padding-left: 8px; padding-top: 4px; list-style: none; }
  .spec-list li {
    font-family: "Oswald", sans-serif; font-weight: 400; font-size: 10px; line-height: 14.5px;
    color: var(--brown-text);
  }
  .spec-list b { font-weight: 600; }

  .skyline {
    position: absolute; left: 0; top: 526px; width: 100%; height: 214px;
    background: linear-gradient(180deg, rgba(255,255,255,0) 0%, rgba(210,210,212,0.55) 60%, rgba(200,200,202,0.7) 100%);
  }

  .weight-badge {
    position: absolute; left: 265px; top: 689px; width: 80px; height: 28px;
    border-radius: 14px; background: var(--ink);
    font-family: "Oswald", sans-serif; font-weight: 500; font-size: 16px; line-height: 28px;
    text-align: center; color: var(--gold-mid);
  }
</style>
</head>
<body>
<main class="canvas">
  <section class="box-front">
    <div class="ornament-band" role="img" aria-label="Gold damask ornamental pattern band"></div>
    <div class="brand-plate">
      <span class="brand-name">Toravelle Works</span>
    </div>

    <h1 class="fragrance-title">Fragrance<br>Name Here</h1>

    <div class="product-details">
      <div class="craft-note">
        <p class="craft-heading">HANDMADE</p>
        <p class="craft-line">Traditional skills handed down</p>
        <p class="craft-line">From generation to generation</p>
      </div>
      <ul class="spec-list">
        <li><b>Material :</b> Wax</li>
        <li><b>Dimensions :</b> Dia 3.8cm Height 7.6cm</li>
        <li>Always use on heat/flame resistant surface</li>
        <li>Ideal for weddings, parties, special events, spa &amp; aromatherapy</li>
      </ul>
    </div>

    <div class="skyline" role="img" aria-label="Line drawing of a city skyline with harbour bridge, opera house and towers"></div>
    <div class="weight-badge">240 g</div>
  </section>
</main>
</body>
</html>
```